Pell Roving needs a flashy flyer to capture new clients.

We need a flyer to send out to potential clients that showcases what we do. We are a small business that repairs heavy equipment on site or at our shop. We would like to see the flyer with black and gray colors.

Target Market(s)

New potential clients.

Industry/Entity Type

Mechanic

Font styles to use
Sans Serif

Colors

Designer to choose only greyscale colors for use in the design.

Requirements
Must have
• Telephone number 801-362-5817
Service area Utah, Wyoming, Idaho, Nevada
"Brands we work on Images Below"
24/7 Emergency Service

https://www.findexample.test/search?
q=Pell+Roving+Equipment+Service+%26+Repair&oq=pell
Nice to have
• What We Do:
Mobile On Site Equipment Repair
Preventative Maintenance
Comprehensive Diagnostics
Diesel & Gas Engine Repair
Air Conditioning Systems
Welding & Fabrication
Hydraulic Cylinder & Hose Repair
Pre Purchase Inspections
Annual Safety Inspections
Pre Purchase Inspections
Should not have
• Open to see some options

```html
<!DOCTYPE html>
<html lang="en">
<head>
<meta charset="UTF-8">
<title>Pell Roving — Heavy Equipment Repair Experts</title>
<link rel="stylesheet" href="https://fonts.googleapis.com/css2?family=Montserrat:wght@400;500;600;700;800&display=swap">
<style>
  :root {
    --ink: #0d0d0d;
    --panel-2: #2a2a2a;
    --grey: #8a8a8a;
    --grey-light: #c9c9c9;
    --white: #ffffff;
    --paper: #f4f4f4;
    --logo-chip: #b9b9b9;
  }
  * { margin: 0; padding: 0; box-sizing: border-box; }
  html, body { width: 675px; height: 1200px; overflow: hidden; background: var(--paper); }
  body { font-family: "Montserrat", Arial, sans-serif; color: var(--white); }

  .flyer {
    position: relative;
    width: 675px; height: 1200px;
    background: linear-gradient(180deg, #151515 0%, #0b0b0b 45%, #1c1c1c 100%);
    overflow: hidden;
  }

  .brand { position: absolute; top: 38px; left: 0; width: 100%; text-align: center; }
  .brand-name { font-size: 44px; font-weight: 800; letter-spacing: 3px; color: var(--grey-light); display: inline-flex; align-items: center; gap: 12px; }
  .brand-square { width: 30px; height: 30px; background: var(--grey-light); display: inline-block; }
  .brand-tag { margin-top: 4px; font-size: 11px; font-weight: 600; letter-spacing: 3px; color: var(--grey); text-transform: uppercase; }
  .brand-rule { width: 300px; height: 1px; background: var(--grey); margin: 10px auto 0; }

  .headline { position: absolute; top: 158px; width: 100%; text-align: center; font-size: 46px; line-height: 1.05; font-weight: 600; text-transform: uppercase; letter-spacing: 0.5px; }

  .service-area { position: absolute; top: 272px; width: 100%; text-align: center; }
  .service-area h2 { display: inline-block; font-size: 17px; font-weight: 700; letter-spacing: 1px; border-bottom: 2px solid var(--white); padding-bottom: 2px; }
  .service-area p { margin-top: 8px; font-size: 18px; font-weight: 500; color: var(--grey-light); }

  .photo-row { position: absolute; top: 340px; left: 60px; width: 555px; height: 150px; display: flex; gap: 10px; }
  .photo { flex: 1; border: 2px solid var(--white); }
  .photo.crane { background: linear-gradient(180deg, #c7ccd1 0%, #9aa0a6 60%, #e6e6e6 100%); }
  .photo.excavator { background: linear-gradient(180deg, #b8bec4 0%, #7d7f72 55%, #dcdcdc 100%); }
  .photo.service-truck { background: linear-gradient(180deg, #aeb4ba 0%, #d4d4d4 60%, #f0f0f0 100%); }

  .truck-photo {
    position: absolute; top: 520px; left: 270px; width: 405px; height: 270px;
    background: linear-gradient(160deg, #9ba1a6 0%, #d8d8d8 50%, #6e6e6e 100%);
  }

  .what-we-do { position: absolute; top: 540px; left: 0; width: 270px; }
  .what-we-do h3 { display: inline-block; background: var(--white); color: var(--ink); font-size: 17px; font-weight: 800; padding: 7px 22px 7px 36px; letter-spacing: 1px; }
  .service-list { list-style: none; margin: 20px 0 0 36px; }
  .service-list li { display: flex; align-items: center; gap: 9px; font-size: 11px; font-weight: 500; color: var(--grey-light); margin-bottom: 16px; white-space: nowrap; }
  .service-list svg { flex: none; }

  .emergency-badge {
    position: absolute; top: 730px; left: 282px; width: 120px; height: 120px; border-radius: 50%;
    background: var(--white); color: var(--ink); border: 5px solid var(--panel-2);
    display: flex; flex-direction: column; align-items: center; justify-content: center; text-align: center;
  }
  .emergency-badge strong { font-size: 34px; font-weight: 800; line-height: 1; }
  .emergency-badge span { font-size: 10px; font-weight: 700; letter-spacing: 0.5px; margin-top: 3px; line-height: 1.2; }

  .call-block { position: absolute; top: 830px; right: 40px; text-align: right; }
  .call-block .label { font-size: 18px; font-weight: 600; letter-spacing: 1px; }
  .call-block .phone { display: flex; align-items: center; gap: 8px; font-size: 36px; font-weight: 800; margin-top: 4px; }

  .brands-band { position: absolute; bottom: 0; left: 0; width: 100%; height: 170px; background: var(--white); }
  .brands-band h4 { position: absolute; top: -30px; left: 36px; font-size: 12px; font-weight: 600; letter-spacing: 1px; color: var(--grey); text-transform: uppercase; }
  .brand-grid { display: grid; grid-template-columns: repeat(7, 1fr); gap: 26px 22px; padding: 38px 36px; }
  .brand-chip { height: 30px; background: var(--logo-chip); border-radius: 3px; }
</style>
</head>
<body>
<main class="flyer">
  <header class="brand">
    <div class="brand-name"><span class="brand-square"></span>PELL ROVING</div>
    <div class="brand-tag">Equipment Service &amp; Repair</div>
    <div class="brand-rule"></div>
  </header>

  <h1 class="headline">Heavy Equipment<br>Repair Experts</h1>

  <section class="service-area">
    <h2>SERVICE AREA</h2>
    <p>Utah | Wyoming | Idaho | Nevada</p>
  </section>

  <div class="photo-row">
    <div class="photo crane" role="img" aria-label="Crane truck parked on a snowy work site"></div>
    <div class="photo excavator" role="img" aria-label="Yellow excavator working on site"></div>
    <div class="photo service-truck" role="img" aria-label="White service truck in the snow"></div>
  </div>

  <div class="truck-photo" role="img" aria-label="White mobile service truck with crane body"></div>

  <section class="what-we-do">
    <h3>WHAT WE DO</h3>
    <ul class="service-list">
      <li><svg width="13" height="13" viewBox="0 0 14 14"><rect x="1" y="1" width="12" height="12" fill="none" stroke="#fff" stroke-width="1.5"/><path d="M3.5 7l2.5 2.5 4.5-5" fill="none" stroke="#fff" stroke-width="1.5"/></svg>Mobile On Site Equipment Repair</li>
      <li><svg width="13" height="13" viewBox="0 0 14 14"><rect x="1" y="1" width="12" height="12" fill="none" stroke="#fff" stroke-width="1.5"/><path d="M3.5 7l2.5 2.5 4.5-5" fill="none" stroke="#fff" stroke-width="1.5"/></svg>Preventative Maintenance</li>
      <li><svg width="13" height="13" viewBox="0 0 14 14"><rect x="1" y="1" width="12" height="12" fill="none" stroke="#fff" stroke-width="1.5"/><path d="M3.5 7l2.5 2.5 4.5-5" fill="none" stroke="#fff" stroke-width="1.5"/></svg>Comprehensive Diagnostics</li>
      <li><svg width="13" height="13" viewBox="0 0 14 14"><rect x="1" y="1" width="12" height="12" fill="none" stroke="#fff" stroke-width="1.5"/><path d="M3.5 7l2.5 2.5 4.5-5" fill="none" stroke="#fff" stroke-width="1.5"/></svg>Diesel &amp; Gas Engine Repair</li>
      <li><svg width="13" height="13" viewBox="0 0 14 14"><rect x="1" y="1" width="12" height="12" fill="none" stroke="#fff" stroke-width="1.5"/><path d="M3.5 7l2.5 2.5 4.5-5" fill="none" stroke="#fff" stroke-width="1.5"/></svg>Air Conditioning Systems</li>
      <li><svg width="13" height="13" viewBox="0 0 14 14"><rect x="1" y="1" width="12" height="12" fill="none" stroke="#fff" stroke-width="1.5"/><path d="M3.5 7l2.5 2.5 4.5-5" fill="none" stroke="#fff" stroke-width="1.5"/></svg>Welding &amp; Fabrication</li>
      <li><svg width="13" height="13" viewBox="0 0 14 14"><rect x="1" y="1" width="12" height="12" fill="none" stroke="#fff" stroke-width="1.5"/><path d="M3.5 7l2.5 2.5 4.5-5" fill="none" stroke="#fff" stroke-width="1.5"/></svg>Hydraulic Cylinder &amp; Hose Repair</li>
      <li><svg width="13" height="13" viewBox="0 0 14 14"><rect x="1" y="1" width="12" height="12" fill="none" stroke="#fff" stroke-width="1.5"/><path d="M3.5 7l2.5 2.5 4.5-5" fill="none" stroke="#fff" stroke-width="1.5"/></svg>Pre Purchase Inspections</li>
      <li><svg width="13" height="13" viewBox="0 0 14 14"><rect x="1" y="1" width="12" height="12" fill="none" stroke="#fff" stroke-width="1.5"/><path d="M3.5 7l2.5 2.5 4.5-5" fill="none" stroke="#fff" stroke-width="1.5"/></svg>Annual Safety Inspections</li>
    </ul>
  </section>

  <div class="emergency-badge">
    <strong>24/7</strong>
    <span>EMERGENCY<br>SERVICE</span>
  </div>

  <section class="call-block">
    <div class="label">CALL US NOW</div>
    <div class="phone">
      <svg width="28" height="28" viewBox="0 0 24 24"><path d="M6.6 10.8a15.1 15.1 0 006.6 6.6l2.2-2.2a1 1 0 011-.25 11.4 11.4 0 003.6.57 1 1 0 011 1V20a1 1 0 01-1 1A17 17 0 013 4a1 1 0 011-1h3.5a1 1 0 011 1 11.4 11.4 0 00.57 3.6 1 1 0 01-.25 1z" fill="#fff"/></svg>
      801-362-5817
    </div>
  </section>

  <footer class="brands-band">
    <h4>Brands we work on</h4>
    <div class="brand-grid">
      <div class="brand-chip"></div><div class="brand-chip"></div><div class="brand-chip"></div><div class="brand-chip"></div><div class="brand-chip"></div><div class="brand-chip"></div><div class="brand-chip"></div>
      <div class="brand-chip"></div><div class="brand-chip"></div><div class="brand-chip"></div><div class="brand-chip"></div><div class="brand-chip"></div><div class="brand-chip"></div><div class="brand-chip"></div>
    </div>
  </footer>
</main>
</body>
</html>
```